I need a logo that demonstrates multiple of the same with one of a distinguishing feature. I would like something that can be recognisable in silhouette format. The business designs Management systems bespoke the to the company helping them pre-qualify for work.
Something that can demonstrate a distinction between a collective group non of which are the same in shape or size, with the largest of these not the distinguished object (or something to that effect).
This is a new business no logo or artwork exists.
Target Market(s)
Small to Medium Size enterprises in the city and rural areas. Looking to make the step up.
Industry/Entity Type
Manufacture
Contact Information for Business Card
room for, Name, Email, phone number
Font styles to use
Requirements
Must have
- would like the silhouette to be recognisable
Nice to have
- would like it to incorporate the name Quarrywell Advisory Systems.
- Would like the same logo to be on both business cards and on corporate shirts
Should not have
- anything that may exclude rural trade or manufacturing.
- I don't want to appear as corporate, just professional

```html
<!DOCTYPE html>
<html lang="en">
<head>
<meta charset="UTF-8">
<title>Quarrywell Advisory Systems – Business Card</title>
<link href="https://fonts.googleapis.com/css2?family=Open+Sans:wght@400;600&display=swap" rel="stylesheet">
<style>
  :root {
    --backdrop: #e6e6e6;
    --card: #ffffff;
    --accent-red: #e31b23;
    --brand-blue: #1e55a8;
    --icon-blue: #0b4ea2;
    --ink: #1a1a1a;
  }
  * { margin: 0; padding: 0; box-sizing: border-box; }
  html, body {
    width: 1200px;
    height: 800px;
    overflow: hidden;
    background: var(--backdrop);
    font-family: "Open Sans", Arial, sans-serif;
  }
  .card {
    position: absolute;
    left: 75px;
    top: 100px;
    width: 1050px;
    height: 600px;
    background: var(--card);
    box-shadow: 0 6px 24px rgba(0,0,0,0.18);
    overflow: hidden;
  }
  .name-tab {
    position: absolute;
    left: 0;
    top: 70px;
    width: 92px;
    height: 22px;
    background: var(--accent-red);
  }
  .holder-name {
    position: absolute;
    left: 108px;
    top: 58px;
    font-size: 34px;
    line-height: 1.2;
    font-weight: 400;
    letter-spacing: 2px;
    color: var(--brand-blue);
  }
  .contact {
    position: absolute;
    display: flex;
    align-items: center;
    gap: 16px;
    font-size: 24px;
    line-height: 1;
    letter-spacing: 1.5px;
    color: var(--brand-blue);
    white-space: nowrap;
  }
  .contact svg { flex: none; }
  .contact-phone { left: 40px; top: 160px; }
  .contact-email { left: 300px; top: 300px; }
  .contact-address { left: 500px; top: 505px; }
  .divider {
    position: absolute;
    left: 430px;
    top: 370px;
    width: 590px;
    height: 24px;
    background: var(--accent-red);
  }
  .brand {
    position: absolute;
    left: 640px;
    top: 165px;
    display: flex;
    align-items: center;
    gap: 18px;
  }
  .brand-mark {
    width: 120px;
    height: 120px;
    background: var(--ink);
    flex: none;
  }
  .brand-name {
    font-size: 34px;
    line-height: 1.08;
    font-weight: 400;
    color: var(--ink);
  }
</style>
</head>
<body>
  <main class="card">
    <div class="name-tab"></div>
    <p class="holder-name">NAME</p>

    <div class="contact contact-phone">
      <svg width="40" height="40" viewBox="0 0 40 40" aria-label="Phone">
        <path d="M10 4 L16 4 L19 13 L14 16 C16 22 18 24 24 26 L27 21 L36 24 L36 30 C36 33 33 36 30 36 C16 35 5 24 4 10 C4 7 7 4 10 4 Z" fill="var(--icon-blue)"/>
      </svg>
      <span class="contact-text">PHONE</span>
    </div>

    <div class="contact contact-email">
      <svg width="54" height="38" viewBox="0 0 54 38" aria-label="Email">
        <rect x="2" y="2" width="50" height="34" fill="none" stroke="#0b4ea2" stroke-width="2"/>
        <polyline points="2,2 27,22 52,2" fill="none" stroke="#0b4ea2" stroke-width="2"/>
        <line x1="2" y1="36" x2="21" y2="18" stroke="#0b4ea2" stroke-width="2"/>
        <line x1="52" y1="36" x2="33" y2="18" stroke="#0b4ea2" stroke-width="2"/>
      </svg>
      <span class="contact-text">EMAIL</span>
    </div>

    <div class="contact contact-address">
      <svg width="54" height="50" viewBox="0 0 54 50" aria-label="Address">
        <polygon points="27,2 52,26 43,26 43,48 11,48 11,26 2,26" fill="var(--icon-blue)"/>
      </svg>
      <span class="contact-text">ADDRESS</span>
    </div>

    <div class="divider"></div>

    <div class="brand">
      <div class="brand-mark"></div>
      <p class="brand-name">Quarrywell<br>Advisory<br>Systems</p>
    </div>
  </main>
</body>
</html>
```